Business Card Design for a Lending Business (Hard Money loans)

We need a business card for our Real Estate Lending business. We do hard Money loans for real estate investors. We have an existing logo we like, see attached. I'd like the business card to mostly include the logo colors, but a bright color pop of some sort would be nice to see also. Card should include Logo, Company Name, Company Address, Employee Name, Cell Phone, Main Phone, Email, Website

Industry/Entity Type

Finance / Lending

Contact Information for Business Card

Logo, Company Name, Company Address, Employee Name, Cell Phone, Main Phone, Email, Website

Requirements
Nice to have
• I'd like the business card to mostly include the logo colors, but a bright color pop of some sort would be nice to see also.

```html
<!DOCTYPE html>
<html lang="en">
<head>
<meta charset="utf-8">
<title>Marlow Ridge Lending – Business Card</title>
<link rel="stylesheet" href="https://fonts.googleapis.com/css2?family=Montserrat:wght@400;500;700&display=swap">
<style>
  :root {
    --navy: #0c1f7a;
    --navy-deep: #07155e;
    --cyan: #15a8e0;
    --ink: #1d1d1d;
    --paper: #ffffff;
    --backdrop: #3a3a3a;
  }
  * { box-sizing: border-box; margin: 0; padding: 0; }
  html, body {
    width: 1200px; height: 1200px; overflow: hidden;
    background: var(--backdrop);
    font-family: "Montserrat", sans-serif;
  }
  .sheet {
    width: 1200px; height: 1200px;
    display: flex; flex-direction: column; align-items: center; justify-content: center;
    gap: 70px;
  }
  .card {
    position: relative;
    width: 840px; height: 480px;
    border-radius: 38px;
    box-shadow: 0 6px 0 var(--cyan), 0 18px 30px rgba(0,0,0,.35);
    overflow: hidden;
  }
  /* Front */
  .card--front { background: var(--paper); }
  .brand {
    position: absolute; top: 110px; left: 0; right: 0;
    display: flex; align-items: center; justify-content: center; gap: 16px;
  }
  .brand__dot {
    width: 34px; height: 34px; border-radius: 50%;
  }
  .brand__name {
    font-weight: 700; font-size: 40px; letter-spacing: 3px; text-transform: uppercase;
  }
  .card--front .brand__dot { background: var(--navy); }
  .card--front .brand__name { color: var(--navy); }

  .person { position: absolute; left: 64px; top: 356px; }
  .person__name {
    color: var(--cyan); font-weight: 700; font-size: 40px; letter-spacing: -1px; line-height: 1;
  }
  .person__role {
    color: var(--ink); font-weight: 500; font-size: 22px; letter-spacing: 1px; margin-top: 4px;
  }
  .divider {
    position: absolute; left: 500px; top: 268px; width: 1.5px; height: 150px; background: #444;
  }
  .contacts {
    position: absolute; left: 540px; top: 276px; list-style: none;
    display: flex; flex-direction: column; gap: 14px;
  }
  .contacts li {
    display: flex; align-items: center; gap: 14px;
    font-size: 20px; color: var(--ink); font-weight: 400;
  }
  .contacts svg { width: 24px; height: 24px; flex: none; }

  /* Back */
  .card--back { background: var(--navy-deep); }
  .pattern {
    position: absolute; inset: 0;
    background: radial-gradient(ellipse at 50% 45%, #1a2f8c 0%, #0f2278 55%, var(--navy-deep) 100%);
  }
  .card--back .brand { top: 300px; }
  .card--back .brand__dot { background: var(--paper); }
  .card--back .brand__name { color: var(--paper); }
</style>
</head>
<body>
<main class="sheet">
  <section class="card card--front" aria-label="Card front">
    <div class="brand">
      <span class="brand__dot"></span>
      <span class="brand__name">Marlow Ridge Lending</span>
    </div>

    <div class="person">
      <p class="person__name">FULL NAME</p>
      <p class="person__role">POSITION</p>
    </div>

    <span class="divider"></span>

    <ul class="contacts">
      <li>
        <svg viewBox="0 0 24 24" aria-hidden="true"><rect x="6" y="2" width="12" height="20" rx="2" fill="none" stroke="#15a8e0" stroke-width="2"/><circle cx="12" cy="18.5" r="1.2" fill="#15a8e0"/></svg>
        (000) 000 0000
      </li>
      <li>
        <svg viewBox="0 0 24 24" aria-hidden="true"><path d="M6.6 10.8c1.4 2.8 3.8 5.1 6.6 6.6l2.2-2.2c.3-.3.7-.4 1-.2 1.1.4 2.3.6 3.6.6.6 0 1 .4 1 1V20c0 .6-.4 1-1 1C10.6 21 3 13.4 3 4c0-.6.4-1 1-1h3.5c.6 0 1 .4 1 1 0 1.3.2 2.5.6 3.6.1.3 0 .7-.2 1z" fill="#15a8e0"/></svg>
        (000) 000 0000
      </li>
      <li>
        <svg viewBox="0 0 24 24" aria-hidden="true"><rect x="2" y="5" width="20" height="14" fill="#15a8e0"/><path d="M2 5l10 8 10-8" fill="none" stroke="#fff" stroke-width="1.6"/></svg>
        email@company.com
      </li>
      <li>
        <svg viewBox="0 0 24 24" aria-hidden="true"><circle cx="12" cy="12" r="9.5" fill="none" stroke="#15a8e0" stroke-width="2"/><ellipse cx="12" cy="12" rx="4" ry="9.5" fill="none" stroke="#15a8e0" stroke-width="1.6"/><path d="M2.5 12h19M4 7h16M4 17h16" stroke="#15a8e0" stroke-width="1.4"/></svg>
        www.company.com
      </li>
    </ul>
  </section>

  <section class="card card--back" aria-label="Card back">
    <div class="pattern" role="img" aria-label="Faint repeating embossed brand pattern across the navy background"></div>
    <div class="brand">
      <span class="brand__dot"></span>
      <span class="brand__name">Marlow Ridge Lending</span>
    </div>
  </section>
</main>
</body>
</html>
```